Design for an iOS and Android app managing shopping list

The app allows you to keep manage shopping lists, each shopping list being made of items to buy...
We need a design for the 3 screens of the app:
a) global view showing list of (shopping) list
b) form enabling to edit the name of a (shopping) list
c) detailed view listing the contents/items of a (shopping) list
d) 1 text page [not illustrated]
2 "alerts" items are also to be designed: confirm and error pop ups.
No specific guidelines, nor logo or whatever.
It will be a free app distributed on iOS and Androïd.
We just want to make it looking nice & very usable for end users.

```html
<!DOCTYPE html>
<html lang="fr">
<head>
<meta charset="utf-8">
<title>List Of Items</title>
<link href="https://fonts.googleapis.com/css2?family=Roboto:wght@400;500&display=swap" rel="stylesheet">
<style>
  :root {
    --brand: #d6545d;
    --brand-dark: #a3323c;
    --on-brand: #ffffff;
    --section-bg: #ebebeb;
    --row-bg: #ffffff;
    --divider: #e3e3e3;
    --text: #505050;
    --muted: #8a8a8a;
    --pill: #e6e6e6;
    --check: #3fae3a;
    --box-border: #c8c8c8;
  }
  * { box-sizing: border-box; margin: 0; padding: 0; }
  html, body {
    width: 1200px; height: 2353px; overflow: hidden;
    background: var(--row-bg);
    font-family: "Roboto", sans-serif;
  }
  .app { width: 1200px; height: 2353px; background: var(--row-bg); }
  .topbar { background: var(--brand); color: var(--on-brand); }
  .status-bar {
    height: 88px; position: relative;
    display: flex; align-items: center; justify-content: space-between;
    padding: 0 24px; font-size: 40px; font-weight: 400;
  }
  .status-left, .status-right { display: flex; align-items: center; gap: 14px; }
  .status-time {
    position: absolute; left: 50%; transform: translateX(-50%);
    font-weight: 400;
  }
  .nav-bar {
    height: 163px; position: relative;
    display: flex; align-items: center; justify-content: center;
  }
  .nav-title { font-size: 55px; font-weight: 400; }
  .nav-back { position: absolute; left: 38px; top: 50%; transform: translateY(-50%); }
  .nav-add {
    position: absolute; right: 38px; top: 50%; transform: translateY(-50%);
    width: 84px; height: 84px; border-radius: 50%; background: var(--brand-dark);
    display: flex; align-items: center; justify-content: center;
  }
  .section-title {
    height: 123px; background: var(--section-bg);
    color: var(--brand); font-size: 49px; font-weight: 400;
    display: flex; align-items: center; padding-left: 30px;
  }
  .item {
    height: 231px; display: flex; align-items: center;
    padding: 0 36px 0 35px; border-bottom: 3px solid var(--divider);
    list-style: none;
  }
  .item:last-child { border-bottom: none; }
  .checkbox {
    width: 58px; height: 58px; border: 3px solid var(--box-border);
    border-radius: 4px; flex: none; display: flex; align-items: center; justify-content: center;
  }
  .item-name { margin-left: 38px; font-size: 46px; font-weight: 400; color: var(--text); flex: 1; }
  .delete {
    width: 117px; height: 117px; border-radius: 50%; background: var(--pill);
    display: flex; align-items: center; justify-content: center; flex: none;
  }
</style>
</head>
<body>
<div class="app">
  <header class="topbar">
    <div class="status-bar">
      <div class="status-left">
        <svg width="128" height="24" viewBox="0 0 128 24">
          <circle cx="12" cy="12" r="10" fill="#fff"/>
          <circle cx="38" cy="12" r="10" fill="#fff"/>
          <circle cx="64" cy="12" r="10" fill="#fff"/>
          <circle cx="90" cy="12" r="9" fill="none" stroke="#fff" stroke-width="2.5"/>
          <circle cx="116" cy="12" r="9" fill="none" stroke="#fff" stroke-width="2.5"/>
        </svg>
        <span>NOVA</span>
        <svg width="44" height="34" viewBox="0 0 44 34">
          <path d="M4 12 A26 26 0 0 1 40 12" fill="none" stroke="#fff" stroke-width="4.5" stroke-linecap="round"/>
          <path d="M11 19 A16 16 0 0 1 33 19" fill="none" stroke="#fff" stroke-width="4.5" stroke-linecap="round"/>
          <circle cx="22" cy="28" r="4.5" fill="#fff"/>
        </svg>
      </div>
      <span class="status-time">4:21 PM</span>
      <div class="status-right">
        <span>100%</span>
        <svg width="92" height="40" viewBox="0 0 92 40">
          <rect x="2" y="4" width="80" height="32" rx="5" fill="none" stroke="#fff" stroke-width="3"/>
          <rect x="7" y="9" width="70" height="22" rx="2" fill="#fff"/>
          <rect x="84" y="14" width="6" height="12" rx="2" fill="#fff"/>
        </svg>
      </div>
    </div>
    <nav class="nav-bar">
      <svg class="nav-back" width="34" height="56" viewBox="0 0 34 56">
        <path d="M30 4 L6 28 L30 52" fill="none" stroke="#fff" stroke-width="4" stroke-linecap="round" stroke-linejoin="round"/>
      </svg>
      <h1 class="nav-title">List Of Items</h1>
      <div class="nav-add">
        <svg width="40" height="40" viewBox="0 0 40 40">
          <path d="M20 4 V36 M4 20 H36" stroke="#fff" stroke-width="6" stroke-linecap="round"/>
        </svg>
      </div>
    </nav>
  </header>

  <section class="list-section">
    <h2 class="section-title">Pending</h2>
    <ul class="items">
      <li class="item"><span class="checkbox"></span><span class="item-name">Serviettes</span><span class="delete"><svg width="48" height="56" viewBox="0 0 48 56"><path d="M4 10 H44 M17 10 V4 H31 V10" fill="none" stroke="#8a8a8a" stroke-width="4"/><path d="M8 14 H40 L37 52 H11 Z" fill="none" stroke="#8a8a8a" stroke-width="4" stroke-linejoin="round"/><path d="M18 20 V46 M24 20 V46 M30 20 V46" stroke="#8a8a8a" stroke-width="3"/></svg></span></li>
      <li class="item"><span class="checkbox"></span><span class="item-name">Oignons</span><span class="delete"><svg width="48" height="56" viewBox="0 0 48 56"><path d="M4 10 H44 M17 10 V4 H31 V10" fill="none" stroke="#8a8a8a" stroke-width="4"/><path d="M8 14 H40 L37 52 H11 Z" fill="none" stroke="#8a8a8a" stroke-width="4" stroke-linejoin="round"/><path d="M18 20 V46 M24 20 V46 M30 20 V46" stroke="#8a8a8a" stroke-width="3"/></svg></span></li>
      <li class="item"><span class="checkbox"></span><span class="item-name">Bougies</span><span class="delete"><svg width="48" height="56" viewBox="0 0 48 56"><path d="M4 10 H44 M17 10 V4 H31 V10" fill="none" stroke="#8a8a8a" stroke-width="4"/><path d="M8 14 H40 L37 52 H11 Z" fill="none" stroke="#8a8a8a" stroke-width="4" stroke-linejoin="round"/><path d="M18 20 V46 M24 20 V46 M30 20 V46" stroke="#8a8a8a" stroke-width="3"/></svg></span></li>
      <li class="item"><span class="checkbox"></span><span class="item-name">Airelles</span><span class="delete"><svg width="48" height="56" viewBox="0 0 48 56"><path d="M4 10 H44 M17 10 V4 H31 V10" fill="none" stroke="#8a8a8a" stroke-width="4"/><path d="M8 14 H40 L37 52 H11 Z" fill="none" stroke="#8a8a8a" stroke-width="4" stroke-linejoin="round"/><path d="M18 20 V46 M24 20 V46 M30 20 V46" stroke="#8a8a8a" stroke-width="3"/></svg></span></li>
      <li class="item"><span class="checkbox"></span><span class="item-name">Foie Gras</span><span class="delete"><svg width="48" height="56" viewBox="0 0 48 56"><path d="M4 10 H44 M17 10 V4 H31 V10" fill="none" stroke="#8a8a8a" stroke-width="4"/><path d="M8 14 H40 L37 52 H11 Z" fill="none" stroke="#8a8a8a" stroke-width="4" stroke-linejoin="round"/><path d="M18 20 V46 M24 20 V46 M30 20 V46" stroke="#8a8a8a" stroke-width="3"/></svg></span></li>
    </ul>
  </section>

  <section class="list-section">
    <h2 class="section-title">Done</h2>
    <ul class="items">
      <li class="item"><span class="checkbox"><svg width="40" height="32" viewBox="0 0 40 32"><path d="M4 16 L15 27 L36 5" fill="none" stroke="#3fae3a" stroke-width="4" stroke-linecap="round" stroke-linejoin="round"/></svg></span><span class="item-name">Saumon Fume</span><span class="delete"><svg width="48" height="56" viewBox="0 0 48 56"><path d="M4 10 H44 M17 10 V4 H31 V10" fill="none" stroke="#8a8a8a" stroke-width="4"/><path d="M8 14 H40 L37 52 H11 Z" fill="none" stroke="#8a8a8a" stroke-width="4" stroke-linejoin="round"/><path d="M18 20 V46 M24 20 V46 M30 20 V46" stroke="#8a8a8a" stroke-width="3"/></svg></span></li>
      <li class="item"><span class="checkbox"><svg width="40" height="32" viewBox="0 0 40 32"><path d="M4 16 L15 27 L36 5" fill="none" stroke="#3fae3a" stroke-width="4" stroke-linecap="round" stroke-linejoin="round"/></svg></span><span class="item-name">Huile Dolive</span><span class="delete"><svg width="48" height="56" viewBox="0 0 48 56"><path d="M4 10 H44 M17 10 V4 H31 V10" fill="none" stroke="#8a8a8a" stroke-width="4"/><path d="M8 14 H40 L37 52 H11 Z" fill="none" stroke="#8a8a8a" stroke-width="4" stroke-linejoin="round"/><path d="M18 20 V46 M24 20 V46 M30 20 V46" stroke="#8a8a8a" stroke-width="3"/></svg></span></li>
    </ul>
  </section>
</div>
</body>
</html>
```